A Maple Syrup Label for a Local Buniness

We are looking for a label for our maple syrup business. Our business currently sells honey, and we are expanding into maple syrup. Our Business name is "Brackley Honey" and we currently have a logo attached below. We would like to incorporate the bee and BH part, but the label could also read "Brackley Farms" with the words maple syrup. We do not want consumers to confuse the maple syrup jars with the honey jars. It should be clear that the jars contain maple syrup. We are open to new designs as well.

```html
<!DOCTYPE html>
<html lang="en">
<head>
<meta charset="UTF-8">
<title>Brackley Farms Maple Syrup Label</title>
<link rel="stylesheet" href="https://fonts.googleapis.com/css2?family=Anton&family=Bitter:wght@400;600&display=swap">
<style>
  :root {
    --page-bg: #a9a9a9;
    --label-bg: #eeeeec;
    --ink: #111111;
    --honey: #f6b400;
    --leaf-wash: #f8c92c;
  }
  html, body {
    margin: 0;
    padding: 0;
    width: 1200px;
    height: 1045px;
    overflow: hidden;
    background: var(--page-bg);
  }
  .label {
    position: absolute;
    left: 266px;
    top: 30px;
    width: 667px;
    height: 985px;
    background: var(--label-bg);
    font-family: "Bitter", Georgia, serif;
    color: var(--ink);
  }
  .label-frame {
    position: absolute;
    left: 26px;
    top: 25px;
    width: 612px;
    height: 932px;
    border: 3px solid var(--ink);
    box-sizing: border-box;
  }
  .brand-mark {
    position: absolute;
    left: 0;
    width: 100%;
    top: 160px;
    display: flex;
    justify-content: center;
    align-items: center;
    gap: 14px;
  }
  .brand-dot {
    width: 22px;
    height: 22px;
    border-radius: 50%;
    background: var(--honey);
  }
  .brand-name {
    font-family: "Bitter", Georgia, serif;
    font-weight: 400;
    font-size: 46px;
    line-height: 1;
    color: var(--ink);
  }
  .product-title {
    position: absolute;
    left: 0;
    top: 0;
    width: 667px;
    height: 640px;
    margin: 0;
  }
  .title-text {
    font-family: "Anton", "Arial Narrow", sans-serif;
    font-weight: 400;
    fill: var(--ink);
  }
  .title-shadow { fill: var(--honey); }
  .rule {
    position: absolute;
    background: var(--ink);
  }
  .rule-h { height: 2px; }
  .rule-v { width: 2px; }
  .farm-line {
    position: absolute;
    left: 58px;
    top: 655px;
    font-size: 29px;
    font-weight: 600;
    line-height: 1;
    margin: 0;
    white-space: nowrap;
  }
  .quality-seal {
    position: absolute;
    left: 500px;
    top: 590px;
    width: 110px;
    height: 110px;
    border: 2px solid var(--ink);
    border-radius: 50%;
    box-sizing: border-box;
  }
  .quality-seal::after {
    content: "";
    position: absolute;
    inset: 20px;
    border-radius: 50%;
    background: var(--honey);
    opacity: 0.8;
  }
  .leaf-art {
    position: absolute;
    left: 64px;
    top: 716px;
    width: 156px;
    height: 128px;
    border-radius: 40% 55% 45% 50%;
    background: radial-gradient(circle at 45% 50%, var(--leaf-wash), #fbdc6e 70%, transparent 72%);
  }
  .purity {
    position: absolute;
    left: 262px;
    top: 716px;
    font-size: 46px;
    line-height: 0.92;
    margin: 0;
  }
  .purity .purity-word { font-weight: 600; }
  .blurb {
    position: absolute;
    left: 451px;
    top: 720px;
    width: 150px;
    font-size: 13px;
    line-height: 1.2;
    margin: 0;
  }
  .origin {
    position: absolute;
    left: 263px;
    top: 818px;
    font-size: 30px;
    font-weight: 600;
    line-height: 1;
    margin: 0;
    white-space: nowrap;
  }
  .dot-row {
    position: absolute;
    left: 174px;
    top: 866px;
    display: flex;
    gap: 23.5px;
  }
  .dot-row span {
    width: 11px;
    height: 11px;
    border-radius: 50%;
    border: 2px solid var(--ink);
    background: var(--honey);
    box-sizing: border-box;
  }
  .grade {
    position: absolute;
    left: 262px;
    top: 918px;
    font-size: 14px;
    line-height: 1;
    margin: 0;
  }
  .volume {
    position: absolute;
    left: 475px;
    top: 894px;
    font-size: 40px;
    line-height: 1;
    margin: 0;
  }
</style>
</head>
<body>
  <main class="label">
    <div class="label-frame"></div>

    <div class="brand-mark">
      <span class="brand-dot"></span>
      <span class="brand-name">Brackley Honey</span>
    </div>

    <svg class="product-title" viewBox="0 0 667 640" role="img" aria-label="Maple Syrup">
      <g aria-hidden="true">
        <text class="title-text title-shadow" x="336" y="481" text-anchor="middle" font-size="178" textLength="412" lengthAdjust="spacingAndGlyphs">MAPLE</text>
        <text class="title-text title-shadow" x="338" y="611" text-anchor="middle" font-size="148" textLength="362" lengthAdjust="spacingAndGlyphs">SYRUP</text>
      </g>
      <text class="title-text" x="332" y="477" text-anchor="middle" font-size="178" textLength="412" lengthAdjust="spacingAndGlyphs">MAPLE</text>
      <text class="title-text" x="334" y="607" text-anchor="middle" font-size="148" textLength="362" lengthAdjust="spacingAndGlyphs">SYRUP</text>
    </svg>

    <div class="rule rule-h" style="left:59px; top:638px; width:425px;"></div>
    <p class="farm-line">TAPPED IN BRACKLEY FARMS</p>
    <div class="quality-seal" role="img" aria-label="Natural ingredients seal"></div>

    <div class="rule rule-h" style="left:59px; top:708px; width:552px;"></div>
    <div class="leaf-art" role="img" aria-label="Sketched maple leaf and seed over a yellow watercolour wash"></div>
    <div class="rule rule-v" style="left:249px; top:708px; height:146px;"></div>
    <p class="purity">100%<br><span class="purity-word">pure</span></p>
    <div class="rule rule-v" style="left:433px; top:708px; height:102px;"></div>
    <p class="blurb">Lorem ipsum dolor sit amet, consectetur adipiscing elit, sed do eiusmod tempor incididunt ut labore</p>
    <div class="rule rule-h" style="left:249px; top:810px; width:362px;"></div>
    <p class="origin">PRODUCT OF CANADA</p>
    <div class="rule rule-h" style="left:59px; top:853px; width:552px;"></div>

    <div class="dot-row">
      <span></span><span></span><span></span><span></span><span></span>
      <span></span><span></span><span></span><span></span><span></span>
    </div>

    <p class="grade">PREMIUM QUALITY</p>
    <p class="volume">500ml</p>
  </main>
</body>
</html>
```